Stationary design for construction company

Want professional stationary and in the future brochures to use for contacting potential customers and existing customers. We are open to suggestions with existing logo. We are a contractor in the construction field that specializes in foundation plastering. We currently do other work but are looking to market and become the only go-to subcontractor for this specialty. I like the red and black contrast and the font which is "biner d". We want to present ourselves as a professional company so potential customers take us seriously.
Dunmore Stucco
86 N. Maple #415
Orem, Utah 84093
801.574.2281 Office
801.846.5037 Mobile
marla@dunmorestucco-example.com
neil@dunmorestucco-example.com
We will need to be able to edit the finished work incase future numbers, addresses and such change.
Thx
Marla
Target Market(s)
New and exiting customers in the building industry
Industry/Entity Type
Construction Company
Font styles to use
Other font styles liked:
- Biner D
Look and feel
Each slider illustrates characteristics of the customer's brand and the style your logo design should communicate.

```html
<!DOCTYPE html>
<html lang="en">
<head>
<meta charset="utf-8">
<title>Dunmore Stucco — Stationery</title>
<link rel="stylesheet" href="https://fonts.googleapis.com/css2?family=Roboto:wght@400;700;900&display=swap">
<style>
  :root {
    --bg: #262626;
    --paper: #ffffff;
    --red: #e3202a;
    --ink: #1d1d1f;
    --dark: #2b2b30;
    --muted: #555;
  }
  * { box-sizing: border-box; margin: 0; padding: 0; }
  html, body { width: 1200px; height: 900px; overflow: hidden; }
  body {
    background: var(--bg);
    font-family: "Roboto", Arial, sans-serif;
    color: var(--ink);
    position: relative;
  }

  /* Brand name */
  .brand {
    display: flex; align-items: center; gap: 8px;
    font-weight: 900; text-transform: uppercase; color: var(--ink);
    letter-spacing: 1px; line-height: 1;
  }
  .brand__square { background: var(--red); flex: none; }

  /* Letterhead */
  .letterhead {
    position: absolute; left: 70px; top: 50px;
    width: 614px; height: 795px;
    background: var(--paper);
  }
  .letterhead .brand { position: absolute; right: 48px; top: 44px; font-size: 22px; }
  .letterhead .brand__square { width: 26px; height: 26px; }

  .footer-rule {
    position: absolute; left: 0; right: 0; top: 700px;
    height: 2px; background: var(--red);
  }
  .contact {
    position: absolute; top: 690px;
    font-size: 11px; line-height: 1.45; color: var(--muted);
  }
  .contact--phone { left: 46px; }
  .contact--mail { left: 232px; }
  .contact--pin { left: 438px; }
  .contact__icon {
    position: absolute; top: 0; left: 0;
    width: 22px; height: 22px; background: var(--paper);
    border: 1.5px solid var(--red);
    display: flex; align-items: center; justify-content: center;
  }
  .contact__text { position: absolute; top: 32px; left: 0; white-space: nowrap; }

  /* Cards */
  .card {
    position: absolute; width: 420px; height: 240px;
    background: var(--paper); overflow: hidden;
  }
  .card--front { left: 740px; top: 90px; }
  .card--back { left: 740px; top: 400px; }

  .front__bar-red {
    position: absolute; left: 0; top: 0; width: 12px; height: 150px; background: var(--red);
  }
  .front__bar-dark {
    position: absolute; right: 0; bottom: 0; width: 12px; height: 150px; background: var(--dark);
  }
  .card--front .brand {
    position: absolute; inset: 0;
    justify-content: center; font-size: 24px;
  }
  .card--front .brand__square { width: 28px; height: 28px; }

  .card--back .brand { position: absolute; left: 20px; top: 28px; font-size: 14px; }
  .card--back .brand__square { width: 18px; height: 18px; }
  .card--back .brand__name { line-height: 1.15; }

  .back__band {
    position: absolute; left: 150px; top: 0; width: 82px; height: 194px; background: var(--red);
    color: #fff; display: flex; flex-direction: column; align-items: center; justify-content: flex-end;
    padding-bottom: 14px; gap: 10px;
  }
  .back__name {
    writing-mode: vertical-rl; transform: rotate(180deg);
    font-size: 13px; font-weight: 700; letter-spacing: .3px;
  }
  .back__details {
    position: absolute; left: 244px; top: 30px; font-size: 8.5px; color: var(--muted);
    display: flex; flex-direction: column; gap: 18px;
  }
  .detail { display: flex; align-items: center; gap: 7px; line-height: 1.45; white-space: nowrap; }
  .detail__dot {
    width: 18px; height: 18px; border-radius: 50%; background: var(--red); flex: none;
    display: flex; align-items: center; justify-content: center;
  }

  .back__accent { position: absolute; background: var(--red); height: 12px; }
  .back__accent--left { left: 18px; bottom: 52px; width: 110px; }
  .back__accent--right { right: 0; bottom: 46px; width: 60px; }

  .back__strip {
    position: absolute; left: 0; right: 0; bottom: 0; height: 46px; background: var(--dark);
    color: #fff; font-size: 9.5px; white-space: nowrap;
    display: flex; align-items: center; gap: 14px; padding-left: 170px;
  }
</style>
</head>
<body>

<section class="letterhead" aria-label="Letterhead">
  <div class="brand"><span class="brand__square"></span><span class="brand__name">Dunmore Stucco</span></div>

  <div class="footer-rule"></div>

  <div class="contact contact--phone">
    <span class="contact__icon">
      <svg width="12" height="12" viewBox="0 0 24 24"><path fill="#e3202a" d="M6.6 10.8a15 15 0 0 0 6.6 6.6l2.2-2.2c.3-.3.7-.4 1-.2 1.1.4 2.300.6 3.600.6.6 0 1 .4 1 1V20c0 .6-.4 1-1 1A17 17 0 0 1 3 4c0-.6.4-1 1-1h3.5c.6 0 1 .4 1 1 0 1.3.2 2.5.6 3.6.1.3 0 .7-.2 1z"/></svg>
    </span>
    <span class="contact__text">801.574.2281 Office<br>801.846.5037 Mobile</span>
  </div>

  <div class="contact contact--mail">
    <span class="contact__icon">
      <svg width="12" height="12" viewBox="0 0 24 24"><path fill="#e3202a" d="M3 5h18v14H3zm2 2v.5l7 5 7-5V7z"/></svg>
    </span>
    <span class="contact__text">marla@dunmorestucco-example.com<br>neil@dunmorestucco-example.com</span>
  </div>

  <div class="contact contact--pin">
    <span class="contact__icon">
      <svg width="12" height="12" viewBox="0 0 24 24"><path fill="#e3202a" d="M12 2a7 7 0 0 0-7 7c0 5 7 13 7 13s7-8 7-13a7 7 0 0 0-7-7zm0 9.5A2.5 2.5 0 1 1 12 6.5a2.5 2.5 0 0 1 0 5z"/></svg>
    </span>
    <span class="contact__text">86 N. Maple #415<br>Orem, Utah 84093</span>
  </div>
</section>

<section class="card card--front" aria-label="Business card front">
  <div class="front__bar-red"></div>
  <div class="front__bar-dark"></div>
  <div class="brand"><span class="brand__square"></span><span class="brand__name">Dunmore Stucco</span></div>
</section>

<section class="card card--back" aria-label="Business card back">
  <div class="brand"><span class="brand__square"></span><span class="brand__name">Dunmore<br>Stucco</span></div>
  <div class="back__accent back__accent--left"></div>
  <div class="back__band">
    <span class="back__name">Dunmore Stucco</span>
    <svg width="18" height="18" viewBox="0 0 24 24"><circle cx="12" cy="12" r="10" fill="none" stroke="#fff" stroke-width="2"/><circle cx="12" cy="10" r="3.2" fill="#fff"/><path d="M6.5 18c1.2-2.4 3.2-3.6 5.5-3.6s4.3 1.2 5.5 3.6" fill="#fff"/></svg>
  </div>
  <div class="back__details">
    <div class="detail">
      <span class="detail__dot"><svg width="10" height="10" viewBox="0 0 24 24"><path fill="#fff" d="M3 5h18v14H3zm2 2v.5l7 5 7-5V7z"/></svg></span>
      <span>marla@dunmorestucco-example.com<br>neil@dunmorestucco-example.com</span>
    </div>
    <div class="detail">
      <span class="detail__dot"><svg width="10" height="10" viewBox="0 0 24 24"><path fill="#fff" d="M12 2a7 7 0 0 0-7 7c0 5 7 13 7 13s7-8 7-13a7 7 0 0 0-7-7zm0 9.5A2.5 2.5 0 1 1 12 6.5a2.5 2.5 0 0 1 0 5z"/></svg></span>
      <span>86 N. Maple #415<br>Orem, Utah 84093</span>
    </div>
  </div>
  <div class="back__accent back__accent--right"></div>
  <div class="back__strip">
    <svg width="14" height="14" viewBox="0 0 24 24"><circle cx="12" cy="12" r="11" fill="#e3202a"/><path fill="#fff" d="M8.6 10.6a9 9 0 0 0 4.8 4.8l1.5-1.5c.2-.2.5-.3.7-.1.8.3 1.6.4 2.4.4v2.6c0 .4-.3.7-.7.7A11 11 0 0 1 6.5 6.7c0-.4.3-.7.7-.7h2.6c0 .8.1 1.6.4 2.4.1.2 0 .5-.1.7z"/></svg>
    <span>801.574.2281 Office</span>
    <span>801.846.5037 Mobile</span>
  </div>
</section>

</body>
</html>
```